Build Steady Practice Growth Through Trust

Design a cover for this book which is designed to help a business go from it's current revenue and treatment acceptance to double (2X) that success and those metrics.

```html
<!DOCTYPE html>
<html lang="en">
<head>
<meta charset="utf-8">
<title>Steady 2X Results – Book Cover</title>
<link rel="stylesheet" href="https://fonts.googleapis.com/css2?family=Oswald:wght@600&family=Barlow+Semi+Condensed:wght@700&family=Arimo:wght@400&display=swap">
<style>
  :root {
    --backdrop: #b9b8b3;
    --cover-paper: #f5f5f4;
    --cover-paper-shade: #e9e9e8;
    --ink-dark: #2b313b;
    --accent-gold: #e2a72a;
  }
  html, body {
    margin: 0;
    padding: 0;
    width: 1200px;
    height: 796px;
    overflow: hidden;
    background: var(--backdrop);
  }
  .stage {
    position: relative;
    width: 1200px;
    height: 796px;
  }
  .book-cover {
    position: absolute;
    left: 331px;
    top: 28px;
    width: 538px;
    height: 740px;
    display: block;
  }
  .kicker { font-family: "Barlow Semi Condensed", "Arial Narrow", sans-serif; font-weight: 700; font-size: 27px; letter-spacing: 3px; }
  .kicker--gold { fill: var(--accent-gold); }
  .kicker--dark { fill: var(--ink-dark); }
  .headline { font-family: "Oswald", "Arial Narrow", sans-serif; font-weight: 600; fill: var(--ink-dark); }
  .numeral { font-family: "Oswald", "Arial Narrow", sans-serif; font-weight: 600; fill: var(--accent-gold); }
  .tagline { font-family: "Arimo", Arial, sans-serif; font-size: 21px; letter-spacing: 1.2px; fill: var(--ink-dark); }
  .author { font-family: "Barlow Semi Condensed", "Arial Narrow", sans-serif; font-weight: 700; font-size: 24px; letter-spacing: 3px; fill: var(--accent-gold); }
  .rule { stroke: var(--ink-dark); stroke-width: 2; }
</style>
</head>
<body>
<main class="stage">
  <svg class="book-cover" viewBox="0 0 683 940" xmlns="http://www.w3.org/2000/svg" aria-label="Book cover: Steady 2X Results">
    <defs>
      <linearGradient id="paper" x1="0" y1="0" x2="1" y2="1">
        <stop offset="0" stop-color="var(--cover-paper)"/>
        <stop offset="1" stop-color="var(--cover-paper-shade)"/>
      </linearGradient>
    </defs>
    <rect class="cover-ground" x="0" y="0" width="683" height="940" fill="url(#paper)"/>

    <text class="kicker kicker--gold" x="345" y="64" text-anchor="middle">THE TRUST PLAYBOOK:</text>
    <text class="kicker kicker--dark" x="345" y="96" text-anchor="middle">BUILD STEADY PRACTICE GROWTH</text>
    <text class="kicker kicker--dark" x="345" y="129" text-anchor="middle">THROUGH TRUST</text>

    <line class="rule" x1="73" y1="158" x2="618" y2="158"/>

    <text class="headline" x="73" y="324" font-size="172" textLength="548" lengthAdjust="spacingAndGlyphs">STEADY</text>

    <text class="numeral" x="345" y="587" font-size="300" text-anchor="middle" textLength="300" lengthAdjust="spacingAndGlyphs">2X</text>

    <text class="headline" x="73" y="760" font-size="168" textLength="548" lengthAdjust="spacingAndGlyphs">RESULTS</text>

    <line class="rule" x1="73" y1="784" x2="618" y2="784"/>

    <text class="tagline" x="345" y="825" text-anchor="middle">Clear Methods to Earn Lasting Patient Trust</text>
    <text class="tagline" x="345" y="850" text-anchor="middle">and Grow Your Practice Year After Year</text>

    <text class="author" x="345" y="888" text-anchor="middle">DANIEL WHITMORE</text>
  </svg>
</main>
</body>
</html>
```